Merry Christmas & A Happy New Year

We need a Greeting Card for this year's Christmas & New Year.

We are a company dealing in the Mechanical Engineering & Manufacturing Industry. Example: Aero Space, Oil & Gas, Marine, etc…

Requirements
Must have
• Company Logo

```html
<!DOCTYPE html>
<html lang="en">
<head>
<meta charset="UTF-8">
<title>Season's Greetings – Norvik Tools</title>
<link rel="stylesheet" href="https://fonts.googleapis.com/css2?family=Crimson+Pro:wght@400;500&display=swap">
<style>
  :root {
    --paper: #ffffff;
    --wine: #7d0a32;
    --ink: #1d1d1d;
    --art-light: #f4f1f0;
    --art-mid: #e9dfdf;
  }
  * { margin: 0; padding: 0; box-sizing: border-box; }
  html, body {
    width: 1200px;
    height: 849px;
    overflow: hidden;
    background: var(--paper);
  }
  .card {
    position: relative;
    width: 1200px;
    height: 849px;
    background: var(--paper);
    font-family: "Crimson Pro", Georgia, serif;
  }
  .card-frame {
    position: absolute;
    left: 177px;
    top: 123px;
    width: 844px;
    height: 597px;
    border: 9px solid var(--wine);
  }
  .greeting-title {
    position: absolute;
    left: 177px;
    top: 166px;
    width: 844px;
    text-align: center;
    color: var(--wine);
    font-weight: 500;
    font-size: 76px;
    line-height: 78px;
    letter-spacing: -0.5px;
  }
  .greeting-wish {
    position: absolute;
    left: 637px;
    top: 363px;
    width: 350px;
    color: var(--ink);
    font-size: 20.5px;
    line-height: 31px;
    letter-spacing: 0.3px;
  }
  .holiday-art {
    position: absolute;
    left: 187px;
    top: 392px;
    width: 430px;
    height: 285px;
    background: linear-gradient(160deg, var(--art-light), var(--art-mid));
  }
  .brand {
    position: absolute;
    left: 762px;
    top: 624px;
    display: flex;
    align-items: center;
    gap: 10px;
  }
  .brand-mark {
    width: 26px;
    height: 26px;
    border-radius: 50%;
    background: var(--wine);
  }
  .brand-name {
    color: var(--wine);
    font-size: 28px;
    line-height: 32px;
    font-weight: 500;
    letter-spacing: 1px;
  }
</style>
</head>
<body>
  <main class="card">
    <div class="card-frame"></div>

    <h1 class="greeting-title">Merry Christmas &amp;<br>A Happy New Year</h1>

    <p class="greeting-wish">May the magic and the wonder of the<br>HOLIDAY SEASON stay with you<br>throughout the coming YEAR!</p>

    <div class="holiday-art" role="img" aria-label="Sketched figure in a Santa hat holding a sign with a star reading Christmas, Happy New Year, standing on a hand-drawn ground line"></div>

    <div class="brand">
      <span class="brand-mark"></span>
      <span class="brand-name">NORVIK TOOLS</span>
    </div>
  </main>
</body>
</html>
```